依頼詳細
PCとスマホデザインの両方納品をいただきますが、
まずはデザインイメージが確認しやすいPCページのみの提案をお願いします。
スマホページは当選者に納品時にお願いしたいと思います。
スマホサイズについて、表示は横幅375pxで作成し、
デザインデータは2倍の横幅750pxのカンバスサイズで作成してください。
(Retinaディスプレイに対応するため)
レスポンシブウェブデザインを意識したデザインでお願いします。

■サイトマップ
添付の画面遷移図をご確認ください。

■参考サイト
https://www.kurumi-p.co.jp/
https://www.m-sorano.co.jp/
https://www.fujino-printing.co.jp/

■内容について
印刷会社のサイトリニューアルになります。
既存サイト
https://www.hinata-printing.co.jp/

■素材写真
画像データについては、フリー素材から流用して
イメージ画像に当て込んでください。
足りない場合は、一旦他のサイトの写真をサンプルとして
入れてください。(サンプルなどの表記をお願いします)
また、購入が必要な写真などを利用した場合、
価格とサイト名を教えてください。

また、Pixmora Stockで定期契約をしていますので、
Pixmora Stockの画像は使用できます。
デザイン時はカンプ画像をお入れいただきますようお願いします。

※採用サイト寄りのサイトにしたいので、使用する画像は
なるべく人物が入っているものを使用してください。

■ワイヤーフレーム
https://mock.plavetta.jp/view/51830427-216b-4c73-9a05-87162534907e-4182/?fullscreen
コンテンツの構成としてワイヤーフレームを作成しましたが
必ずしもワイヤーフレームの通りではなくて大丈夫です。
TOPページに配置するコンテンツを見ていただき、デザインは
デザイナーの皆様におまかせしたいと思います。

----------------------------------------------------------------------------
【制作物に対するお願い】

■フォントについて
・無料で使えるフォントで作成をお願いします。
・OSに紐づくフォントの使用は控えていただければと思います (ヒラギノなど)

ページ数
1ページ
希望イメージ
シンプル 複雑
単色 カラフル
暗い 明るい
日常 高級
遊び心 厳粛
未来的 伝統的
女性的 男性的
希望する色
青系、既存サイトに載っているロゴのイメージでお願いします。
納品ファイル
• 高解像度JPG (.jpg)
• イラストレーター形式 (.ai)
• フォトショップ形式 (.psd)
補足説明
上記のいずれか1つ(アウトラインありとなしの2つ)と高解像度JPGを納品お願いします。
adobe XDでの納品も可能です。

```html
<!DOCTYPE html>
<html lang="ja">
<head>
<meta charset="UTF-8">
<title>株式会社ヒナタ印刷</title>
<link href="https://fonts.googleapis.com/css2?family=Montserrat:wght@400;500;600;700&family=Noto+Sans+JP:wght@400;500;700;900&display=swap" rel="stylesheet">
<style>
:root{
  --blue:#1d4f9e;
  --blue-dark:#163a75;
  --blue-light:#3a7bd5;
  --navy:#2b2f3a;
  --ink:#222a36;
  --muted:#6b7380;
  --line:#d7dce4;
  --pale:#f2f4f8;
  --white:#fff;
}
*{box-sizing:border-box;margin:0;padding:0}
html,body{width:1200px;height:3548px;overflow:hidden}
body{font-family:"Noto Sans JP",sans-serif;color:var(--ink);background:var(--white);font-size:14px;line-height:1.8}
.en{font-family:"Montserrat",sans-serif}
a{color:inherit;text-decoration:none}

/* header */
.site-header{height:88px;display:flex;align-items:center;justify-content:space-between;padding:0 32px}
.brand{display:flex;align-items:center;gap:12px}
.brand-mark{width:34px;height:34px;background:var(--blue)}
.brand-name{font-size:26px;font-weight:900;color:var(--blue);letter-spacing:.04em;line-height:1}
.brand-name small{font-size:12px;font-weight:900;margin-right:6px}
.global-nav{display:flex;align-items:center;gap:34px;font-size:14px;font-weight:500}
.contact-btn{display:flex;align-items:center;gap:8px;border:1px solid var(--ink);padding:9px 20px;font-family:"Montserrat",sans-serif;font-weight:500}

/* hero */
.hero{position:relative;height:512px;background:linear-gradient(120deg,#cfd4da 0%,#9aa3ad 40%,#e6e3dd 60%,#7c8590 100%);display:flex;flex-direction:column;align-items:center;justify-content:center;color:var(--white);text-align:center}
.hero::before{content:"";position:absolute;inset:0;background:rgba(20,30,50,.32)}
.hero > *{position:relative}
.hero-copy{font-size:46px;font-weight:700;line-height:1.45;letter-spacing:.06em;text-shadow:0 2px 10px rgba(0,0,0,.35)}
.hero-sub{margin-top:14px;font-size:22px;letter-spacing:.2em;font-weight:500}
.hero-side{position:absolute;left:18px;top:230px;writing-mode:vertical-rl;font-size:11px;letter-spacing:.3em}

/* common heads */
.label{font-family:"Montserrat",sans-serif;font-size:13px;font-weight:600;letter-spacing:.1em}
.title{font-size:28px;font-weight:700;color:var(--blue);line-height:1.4}
.more{font-size:12px;display:flex;align-items:center;gap:8px}

/* about */
.about{height:560px;padding:110px 160px 0;display:flex;gap:90px}
.about-head{width:280px}
.about-head .title{margin-top:10px}
.about-body{flex:1;font-size:14px;line-height:2.1}
.about-body p+p{margin-top:18px}

/* business */
.business{height:360px;display:flex}
.business-info{width:600px;position:relative;background:linear-gradient(135deg,#4a6fa8,#243f74);color:var(--white);padding:76px 0 0 160px}
.business-info .title{color:var(--white);margin-top:4px}
.business-info p{margin-top:12px;font-size:13px;width:380px;line-height:1.9}
.btn-outline{display:inline-flex;align-items:center;gap:20px;border:1px solid currentColor;padding:8px 26px;font-size:13px;margin-top:22px}
.business-photo{flex:1;background:linear-gradient(120deg,#c9b9c2,#e8dfcf 40%,#8fb1c9 70%,#d7c6a5)}

/* works */
.works{height:640px;padding:100px 160px 0}
.section-head{display:flex;justify-content:space-between;align-items:flex-end}
.section-head .title{margin-top:4px}
.works-list{display:flex;gap:40px;margin-top:40px}
.work-card{width:267px}
.work-thumb{height:200px;background:linear-gradient(135deg,#eef0f3,#c9d2dc)}
.work-card:nth-child(2) .work-thumb{background:linear-gradient(135deg,#c79a5a,#7d5a3a)}
.work-card h3{font-size:14px;font-weight:700;margin-top:16px;line-height:1.6}
.work-card span{display:block;font-size:11px;color:var(--muted);margin-top:6px}

/* links panels */
.panels{height:340px;display:flex}
.panel{flex:1;position:relative;display:flex;flex-direction:column;align-items:center;justify-content:center;color:var(--white);text-align:center}
.panel-company{background:linear-gradient(135deg,#6d747d,#3b424c)}
.panel-submit{background:linear-gradient(135deg,#bfc6cf,#7b8592)}
.panel::before{content:"";position:absolute;inset:0;background:rgba(10,20,40,.35)}
.panel > *{position:relative}
.panel strong{font-size:30px;font-weight:700;letter-spacing:.08em}
.panel .en{font-size:14px;letter-spacing:.12em;margin-top:4px}

/* news */
.news{height:330px;padding:80px 160px 0;display:flex;gap:30px}
.side-head{width:210px}
.side-head .title{margin-top:4px;font-size:26px}
.side-head .btn-outline{color:var(--blue);margin-top:16px;padding:5px 22px;font-size:12px}
.news-list{flex:1;list-style:none}
.news-item{border-bottom:1px solid var(--line);padding:10px 0 14px}
.news-item time{display:block;font-size:12px;color:var(--blue);font-family:"Montserrat",sans-serif}
.news-item p{font-size:13px}

/* blog */
.blog{height:370px;padding:10px 160px 0;display:flex;gap:30px}
.blog-list{flex:1;display:flex;gap:24px}
.blog-card{width:215px}
.blog-thumb{height:140px;background:linear-gradient(135deg,#9aa4b0,#4f5966)}
.blog-card:nth-child(2) .blog-thumb{background:linear-gradient(135deg,#c8b49a,#6e6557)}
.blog-card:nth-child(3) .blog-thumb{background:linear-gradient(135deg,#d8d2c8,#8a7f70)}
.blog-card p{font-size:13px;font-weight:500;margin-top:10px;line-height:1.6}
.blog-card time{font-size:11px;color:var(--muted);font-family:"Montserrat",sans-serif}

/* footer */
.site-footer{height:348px;background:var(--navy);color:var(--white);padding:76px 160px 0}
.footer-top{display:flex;justify-content:space-between;align-items:center}
.site-footer .brand-name{color:var(--white);font-size:32px}
.site-footer .brand-mark{background:var(--blue-light);width:42px;height:42px}
.footer-address{font-size:13px;line-height:1.9}
.footer-address b{font-size:15px;font-family:"Montserrat",sans-serif}
.footer-bottom{margin-top:70px;padding-top:22px;border-top:1px solid rgba(255,255,255,.2);display:flex;justify-content:space-between;font-size:12px}
.footer-links{display:flex;gap:26px}
</style>
</head>
<body>

<header class="site-header">
  <div class="brand"><span class="brand-mark"></span><span class="brand-name"><small>株式会社</small>ヒナタ印刷</span></div>
  <nav class="global-nav">
    <a href="#">事業案内</a><a href="#">入稿について</a><a href="#">事業紹介</a><a href="#">会社案内</a>
    <a href="#" class="contact-btn">
      <svg width="16" height="12" viewBox="0 0 16 12"><rect x=".5" y=".5" width="15" height="11" fill="none" stroke="currentColor"/><path d="M1 1l7 6 7-6" fill="none" stroke="currentColor"/></svg>Contact</a>
  </nav>
</header>

<section class="hero" role="img" aria-label="印刷機で刷り上がった色見本の写真">
  <span class="hero-side en">PRINTING</span>
  <h1 class="hero-copy">"お客様の視点"を第一に<br>幅広い印刷のご提案</h1>
  <p class="hero-sub en">PRINTING SERVICE</p>
</section>

<section class="about">
  <div class="about-head">
    <p class="label">ABOUT US</p>
    <h2 class="title">ヒナタ印刷は<br>お客様と共に考えます</h2>
  </div>
  <div class="about-body">
    <p>新潟県の県央地域で創立以来、冊子、伝票、封筒、パッケージ、事務用品まで幅広い印刷物を手がけてまいりました。地域の皆様に支えられ、一つひとつの仕事に誠実に向き合ってきました。</p>
    <p>しかし印刷を取り巻く環境は大きく変化し、紙媒体だけでなくデジタルとの連携も求められています。私たちは時代に合わせた新しい技術と、これまで培った確かな品質を大切にしています。</p>
    <p>お客様が「何を必要としているのか」をまず考え、企画の段階から一緒に取り組むことで、想いが伝わる印刷物をお届けいたします。</p>
    <p>"お客様の視点"を第一に、社員一同これからも信頼されるものづくりを続けてまいります。</p>
  </div>
</section>

<section class="business">
  <div class="business-info" role="img" aria-label="印刷機を操作する工場の写真に青い重ね">
    <p class="label">BUSINESS</p>
    <h2 class="title">業務案内</h2>
    <p>ヒナタ印刷では、企画・デザインから印刷・加工・発送まで一貫してお手伝いしております。お気軽にご相談ください。</p>
    <a href="#" class="btn-outline">詳しく見る <span>→</span></a>
  </div>
  <div class="business-photo" role="img" aria-label="色見本とルーペの写真"></div>
</section>

<section class="works">
  <div class="section-head">
    <div><p class="label" style="color:var(--blue)">WORKS</p><h2 class="title">事例紹介</h2></div>
    <a href="#" class="more">一覧をみる <span>→</span></a>
  </div>
  <div class="works-list">
    <article class="work-card"><div class="work-thumb" role="img" aria-label="パンフレット制作例の写真"></div><h3>こちらに事例タイトルが入ります。テキストテキストテキスト</h3><span>事例カテゴリ名</span></article>
    <article class="work-card"><div class="work-thumb" role="img" aria-label="パッケージ制作例の写真"></div><h3>こちらに事例タイトルが入ります。テキストテキストテキスト</h3><span>事例カテゴリ名</span></article>
    <article class="work-card"><div class="work-thumb" role="img" aria-label="冊子制作例の写真"></div><h3>こちらに事例タイトルが入ります。テキストテキストテキスト</h3><span>事例カテゴリ名</span></article>
  </div>
</section>

<section class="panels">
  <a href="#" class="panel panel-company" role="img" aria-label="工場内の印刷機の写真"><strong>会社概要</strong><span class="en">COMPANY</span></a>
  <a href="#" class="panel panel-submit" role="img" aria-label="キーボードとディスクの写真"><strong>入稿について</strong><span class="en">SUBMIT A MANUSCRIPT</span></a>
</section>

<section class="news">
  <div class="side-head">
    <p class="label">NEWS</p><h2 class="title">新着情報</h2>
    <a href="#" class="btn-outline">一覧をみる <span>→</span></a>
  </div>
  <ul class="news-list">
    <li class="news-item"><time>2022.10.20</time><p>こちらにテキストが入ります。テキストテキストテキストテキストテキスト。</p></li>
    <li class="news-item"><time>2022.10.20</time><p>こちらにテキストが入ります。テキストテキストテキストテキストテキスト。</p></li>
    <li class="news-item"><time>2022.10.20</time><p>こちらにテキストが入ります。テキストテキストテキストテキストテキスト。</p></li>
  </ul>
</section>

<section class="blog">
  <div class="side-head">
    <p class="label">BLOG</p><h2 class="title">ブログ</h2>
    <a href="#" class="btn-outline">一覧をみる <span>→</span></a>
  </div>
  <div class="blog-list">
    <article class="blog-card"><div class="blog-thumb" role="img" aria-label="社内研修の様子の写真"></div><p>こちらにテキストが入ります。テキストテキストテキスト</p><time>2022.10.20</time></article>
    <article class="blog-card"><div class="blog-thumb" role="img" aria-label="会議室での説明会の写真"></div><p>こちらにテキストが入ります。テキストテキストテキスト</p><time>2022.10.20</time></article>
    <article class="blog-card"><div class="blog-thumb" role="img" aria-label="オフィス風景の写真"></div><p>こちらにテキストが入ります。テキストテキストテキスト</p><time>2022.10.20</time></article>
  </div>
</section>

<footer class="site-footer">
  <div class="footer-top">
    <div class="brand"><span class="brand-mark"></span><span class="brand-name"><small>株式会社</small>ヒナタ印刷</span></div>
    <div class="footer-address">
      <p>〒000-0000　新潟県みどり市中央1丁目2番3号</p>
      <p><b>TEL:025-000-4821</b>（代）　<b>FAX:025-000-4837</b></p>
    </div>
  </div>
  <div class="footer-bottom">
    <div class="footer-links"><a href="#">お問い合わせ</a><a href="#">プライバシーポリシー</a><a href="#">サイトマップ</a></div>
    <p class="en">Copyright © 株式会社ヒナタ印刷</p>
  </div>
</footer>

</body>
</html>
```